Flyer für Zeitarbeitsfirma
Zielgruppe
Wir sind eine Zeitarbeitsfirma in der Pflege! Unsere Kunden sind Krankenhäuser und Pflegeheime
Aufgabenstellung
Wir möchten eine Art Flyer als erste Seite einer Bewerbungsmappe.
Überschrift: Bewerbung als Personaldienstleister
Warum K7-CURAVIT?
Wir bieten entscheidende Unterschiede:
1 Tag KOSTENFREI
(Vermindern Sie Ihr Risiko für schlechtes Zeitarbeitspersonal)
5 Tage günstiger Einarbeitungstarif
anschließend erhalten Sie eine Preisgarantie fürs gesamte Jahr
PLUS kostenfreie Übernahme unserer Mitarbeiter
Worauf warten Sie noch?
Wir freuen uns auf eine tolle Zusammenarbeit!
www.kobalt-7.de

```html
<!DOCTYPE html>
<html lang="de">
<head>
<meta charset="utf-8">
<title>K7-CURAVIT – Bewerbung als Personaldienstleister</title>
<link href="https://fonts.googleapis.com/css2?family=Krona+One&family=Poppins:wght@300;600&display=swap" rel="stylesheet">
<style>
  :root {
    --stage: #8fa3a3;
    --paper: #f1f2f4;
    --navy: #0b3868;
    --navy-deep: #083060;
    --blue: #0f78c0;
    --blue-mid: #1a88cc;
    --cyan: #4fb8e0;
    --white: #ffffff;
  }
  * { margin: 0; padding: 0; box-sizing: border-box; }
  html, body { width: 1200px; height: 1118px; overflow: hidden; background: var(--stage); }
  .flyer {
    position: absolute; left: 226px; top: 29px;
    width: 748px; height: 1060px;
    background: var(--paper); overflow: hidden;
    box-shadow: 0 6px 24px rgba(0,0,0,.18);
  }
  .flyer__shapes { position: absolute; inset: 0; }
  .top-bar { position: absolute; left: 101px; top: 0; width: 547px; height: 14px; background: var(--cyan); }
  .headline {
    position: absolute; top: 52px; left: 0; width: 100%;
    text-align: center; font-family: "Krona One", sans-serif;
    font-size: 29px; line-height: 35px; color: var(--navy); letter-spacing: .5px;
  }
  .pill {
    position: absolute; left: 118px; top: 602px; width: 493px; height: 41px;
    border-radius: 21px; background: var(--navy);
    display: flex; align-items: center; justify-content: center;
    font-family: "Krona One", sans-serif; font-size: 16px; color: var(--paper);
  }
  .benefits__lead {
    position: absolute; left: 119px; top: 662px;
    font-family: "Krona One", sans-serif; font-size: 16px; color: #e8eef5;
  }
  .benefits {
    position: absolute; left: 119px; top: 700px; list-style: none;
    font-family: "Poppins", sans-serif; font-weight: 600; font-size: 13.5px; color: #f0f4f8;
  }
  .benefits li { position: relative; padding-left: 27px; margin-bottom: 17px; line-height: 18px; }
  .benefits li svg { position: absolute; left: 1px; top: 3px; }
  .benefits .note { display: block; font-weight: 300; font-size: 14px; }
  .cta-pill {
    position: absolute; left: 199px; top: 915px; width: 349px; height: 39px;
    border: 2px solid var(--blue-mid); border-radius: 20px;
    display: flex; align-items: center; justify-content: center;
    font-family: "Krona One", sans-serif; font-size: 16px; color: var(--paper);
  }
  .closing {
    position: absolute; top: 964px; left: 0; width: 100%; text-align: center;
    font-family: "Krona One", sans-serif; font-size: 22px; line-height: 30px; color: var(--paper);
  }
</style>
</head>
<body>
<main class="flyer">
  <svg class="flyer__shapes" width="748" height="1060" viewBox="0 0 748 1060">
    <defs>
      <linearGradient id="photoTone" x1="0" y1="0" x2="1" y2="0">
        <stop offset="0" stop-color="#2f4e78"/>
        <stop offset=".45" stop-color="#9a7a6a"/>
        <stop offset=".55" stop-color="#e89a5c"/>
        <stop offset="1" stop-color="#4e6e96"/>
      </linearGradient>
      <linearGradient id="photoFade" x1="0" y1="0" x2="0" y2="1">
        <stop offset="0" stop-color="#f1f2f4" stop-opacity="1"/>
        <stop offset=".3" stop-color="#f1f2f4" stop-opacity="0"/>
        <stop offset=".8" stop-color="#f1f2f4" stop-opacity="0"/>
        <stop offset="1" stop-color="#f1f2f4" stop-opacity=".9"/>
      </linearGradient>
      <linearGradient id="mainBlue" x1="0" y1="0" x2="0" y2="1">
        <stop offset="0" stop-color="#1b86c9"/>
        <stop offset="1" stop-color="#0d6fb6"/>
      </linearGradient>
    </defs>
    <g role="img" aria-label="Foto: Handschlag im Doppelbelichtungs-Stil mit Silhouetten von Fachkräften vor einer Stadtskyline im Abendlicht">
      <rect x="0" y="100" width="748" height="340" fill="url(#photoTone)" opacity=".75"/>
      <rect x="0" y="100" width="748" height="340" fill="url(#photoFade)"/>
    </g>
    <path d="M0 352 C180 470 420 530 748 456 L748 1060 L0 1060 Z" fill="var(--navy)"/>
    <path d="M0 400 C200 520 480 560 748 478 L748 1060 L0 1060 Z" fill="var(--paper)"/>
    <path d="M0 438 C230 560 500 580 748 520 L748 1060 L0 1060 Z" fill="var(--cyan)"/>
    <path d="M0 458 C240 585 510 600 748 548 L748 1060 L0 1060 Z" fill="url(#mainBlue)"/>
    <path d="M0 930 C200 880 300 860 374 860 C450 860 550 880 748 930 L748 1060 L0 1060 Z" fill="var(--cyan)"/>
    <path d="M0 960 C200 900 300 876 374 876 C450 876 560 900 748 960 L748 1060 L0 1060 Z" fill="var(--navy)"/>
  </svg>

  <div class="top-bar"></div>
  <h1 class="headline">BEWERBUNG ALS<br>PERSONALDIENSTLEISTER</h1>

  <div class="pill">Warum K7-CURAVIT?</div>
  <p class="benefits__lead">Wir bieten entscheidende Unterschiede:</p>
  <ul class="benefits">
    <li><svg width="13" height="13" viewBox="0 0 13 13"><circle cx="6.5" cy="6.5" r="6.5" fill="#f0f4f8"/><path d="M3.6 6.7 L5.6 8.6 L9.4 4.6" stroke="#0f78c0" stroke-width="1.8" fill="none"/></svg>1 Tag KOSTENFREI<span class="note">(Vermindern Sie Ihr Risiko für schlechtes Zeitarbeitspersonal)</span></li>
    <li><svg width="13" height="13" viewBox="0 0 13 13"><circle cx="6.5" cy="6.5" r="6.5" fill="#f0f4f8"/><path d="M3.6 6.7 L5.6 8.6 L9.4 4.6" stroke="#0f78c0" stroke-width="1.8" fill="none"/></svg>5 Tage günstiger Einarbeitungstarif</li>
    <li><svg width="13" height="13" viewBox="0 0 13 13"><circle cx="6.5" cy="6.5" r="6.5" fill="#f0f4f8"/><path d="M3.6 6.7 L5.6 8.6 L9.4 4.6" stroke="#0f78c0" stroke-width="1.8" fill="none"/></svg>anschließend erhalten Sie eine Preisgarantie fürs gesamte Jahr</li>
    <li><svg width="13" height="13" viewBox="0 0 13 13"><circle cx="6.5" cy="6.5" r="6.5" fill="#f0f4f8"/><path d="M3.6 6.7 L5.6 8.6 L9.4 4.6" stroke="#0f78c0" stroke-width="1.8" fill="none"/></svg>PLUS kostenfreie Übernahme unserer Mitarbeiter</li>
  </ul>

  <div class="cta-pill">Worauf warten Sie noch?</div>
  <p class="closing">Wir freuen uns auf eine tolle<br>Zusammenarbeit!</p>
</main>
</body>
</html>
```